Christmas Postcard a manufacturer of skirting boards

Relaunch of the Christmas greetings Postcard of a company manufacturing premium quality skirting boards from real wood. Please refer to http://www.brumholt-profile.example/

- Christmas greetings Postcard 105 mm x 210 mm (card will be sent without envelope)

frontside:
- your graphic design, including
- Logo on the card
- Greetings "Frohe Weihnachten und ein erfolgreiches neues Jahr" on the card (front)
- insert Wooden Earring(s) - for recognition!

backside: (on the left)
"Wir bedanken uns für die partnerschaftliche Zusammenarbeit und freuen uns darauf, Sie auch im Jahr 2016 mit unseren Angeboten, Ideen und Know-how bei der Verwirklichung Ihrer Vorhaben zu unterstützen. (see pdf´s)

Ihnen und Ihren Mitarbeitern wünschen wir ein zauberhaftes Weihnachtsfest und für das neue Jahr Gesundheit, Glück, Erfolg und Freude."

Signatures (see pdf`s)

backside (on the right):
Adress field

------
The pdf´s from last years are just for the color mood. Fresh, modern design appreciated, no comic style.

Industry/Entity Type

It Company

Requirements
Must have
• "Wooden Earring(s)"

```html
<!DOCTYPE html>
<html lang="de">
<head>
<meta charset="utf-8">
<title>Brumholt – Weihnachtskarte</title>
<link rel="stylesheet" href="https://fonts.googleapis.com/css2?family=Comfortaa:wght@400;700&family=Didact+Gothic&family=Mulish:wght@800&display=swap">
<style>
  :root {
    --page: #ffffff;
    --brand-red: #bd2634;
    --wood-tan: #e3b27c;
    --circle-tan: rgba(196, 160, 122, 0.78);
    --photo-dark: #2b2b2b;
    --photo-mid: #6d6d6d;
    --photo-light: #c9c9c9;
    --ink: #1b1b1b;
    --white: #ffffff;
    --back-lilac: #ece9f1;
    --back-peach: #efd6c9;
    --back-cream: #f6f0e2;
  }
  * { box-sizing: border-box; margin: 0; padding: 0; }
  html, body { width: 1200px; height: 1200px; overflow: hidden; background: var(--page); }
  .canvas { position: relative; width: 1200px; height: 1200px; }

  .card { position: absolute; left: 42px; width: 1116px; overflow: hidden;
          box-shadow: 0 3px 10px rgba(0,0,0,0.25); }

  /* Front */
  .card--front { top: 36px; height: 558px; }
  .front-photo { position: absolute; inset: 0 0 22px 0;
    background:
      radial-gradient(ellipse at 82% 12%, var(--photo-light) 0%, transparent 45%),
      radial-gradient(ellipse at 30% 55%, var(--photo-mid) 0%, transparent 60%),
      linear-gradient(135deg, #3a3a3a 0%, var(--photo-dark) 55%, #4a4a4a 100%); }
  .front-band-red { position: absolute; left: 0; right: 0; top: 536px; height: 12px; background: var(--brand-red); }
  .front-band-wood { position: absolute; left: 0; right: 0; top: 548px; height: 10px; background: var(--wood-tan); }

  .brand { position: absolute; left: 26px; top: 28px; width: 360px; color: var(--white); }
  .brand-row { display: flex; align-items: center; gap: 14px; }
  .brand-mark { width: 34px; height: 34px; background: var(--brand-red); }
  .brand-name { font-family: "Comfortaa", sans-serif; font-weight: 700; font-size: 44px; letter-spacing: 2px; line-height: 1; }
  .brand-rule { height: 3px; background: var(--white); margin-top: 4px; }
  .brand-tagline { font-family: "Didact Gothic", sans-serif; font-size: 16px; letter-spacing: 3px; margin: 4px 0 0 54px; }

  .front-url { position: absolute; left: 56px; top: 492px; font-family: "Comfortaa", sans-serif;
    font-size: 20px; letter-spacing: 5px; color: var(--white); }

  .greeting-disc { position: absolute; left: 730px; top: 124px; width: 344px; height: 344px;
    border-radius: 50%; background: var(--circle-tan); }
  .greeting { position: absolute; left: 730px; top: 216px; width: 344px; text-align: center;
    font-family: "Comfortaa", sans-serif; font-size: 33px; line-height: 34px; letter-spacing: 3px; color: var(--white); }

  /* Back */
  .card--back { top: 606px; height: 558px;
    background:
      radial-gradient(ellipse at 95% 80%, var(--back-peach) 0%, transparent 55%),
      radial-gradient(ellipse at 0% 75%, var(--back-cream) 0%, transparent 50%),
      var(--back-lilac); }
  .back-disc { position: absolute; left: 162px; top: -82px; width: 792px; height: 792px; border-radius: 50%;
    background: radial-gradient(circle at 50% 35%, rgba(255,255,255,0.95) 0%, rgba(255,255,255,0.55) 70%, rgba(255,255,255,0.35) 100%); }
  .message { position: absolute; left: 0; right: 0; text-align: center; font-family: "Didact Gothic", sans-serif;
    font-size: 19px; line-height: 21px; color: var(--ink); }
  .message--thanks { top: 98px; }
  .message--wishes { top: 187px; }

  .signer { position: absolute; top: 272px; width: 240px; text-align: center; }
  .signer-mark { display: block; margin: 0 auto; width: 200px; height: 64px; }
  .signer-name { margin-top: 18px; font-family: "Mulish", sans-serif; font-weight: 800; font-size: 14px; color: var(--ink); }
  .signer--1 { left: 184px; }
  .signer--2 { left: 449px; }
  .signer--3 { left: 716px; }

  .address, .contact { position: absolute; font-family: "Mulish", sans-serif; font-weight: 800;
    font-size: 14px; line-height: 16px; color: var(--ink); }
  .address { left: 18px; top: 464px; }
  .contact { right: 24px; top: 480px; text-align: right; }

  .back-band { position: absolute; left: 0; right: 0; bottom: 0; height: 22px; background: var(--brand-red);
    color: var(--white); text-align: center; font-family: "Mulish", sans-serif; font-weight: 800;
    font-size: 15px; line-height: 22px; letter-spacing: 2px; }
</style>
</head>
<body>
<main class="canvas">
  <section class="card card--front">
    <div class="front-photo" role="img" aria-label="Schwarzweißfoto eines verschneiten Tannenzweigs mit einem hängenden Holzohrring im Schneefall"></div>
    <div class="front-band-red"></div>
    <div class="front-band-wood"></div>

    <div class="brand">
      <div class="brand-row">
        <span class="brand-mark"></span>
        <span class="brand-name">brumholt</span>
      </div>
      <div class="brand-rule"></div>
      <div class="brand-tagline">Leistenfabrik Holzimport</div>
    </div>

    <div class="front-url">www.brumholt-profile.example</div>

    <div class="greeting-disc"></div>
    <p class="greeting">Frohe<br>Weihnachten<br>und ein<br>erfolgreiches<br>neues Jahr</p>
  </section>

  <section class="card card--back">
    <div class="back-disc"></div>
    <p class="message message--thanks">Wir bedanken uns für die partnerschaftliche Zusammenarbeit und freuen<br>uns darauf, Sie auch im Jahr 2016 mit unseren Angeboten, Ideen und<br>Know-how bei der Verwirklichung Ihrer Vorhaben zu unterstützen</p>
    <p class="message message--wishes">Ihnen und Ihren Mitarbeitern wünschen wir ein zauberhaftes Weihnachtsfest<br>und für das neue Jahr Gesundheit, Glück, Erfolg und Freude.</p>

    <div class="signer signer--1">
      <svg class="signer-mark" viewBox="0 0 200 64" role="img" aria-label="Unterschrift Jens Brumholt"><rect x="10" y="22" width="180" height="22" rx="11" fill="rgba(0,0,0,0.06)"/></svg>
      <p class="signer-name">Jens Brumholt</p>
    </div>
    <div class="signer signer--2">
      <svg class="signer-mark" viewBox="0 0 200 64" role="img" aria-label="Unterschrift Marion Brumholt"><rect x="10" y="22" width="180" height="22" rx="11" fill="rgba(0,0,0,0.06)"/></svg>
      <p class="signer-name">Marion Brumholt</p>
    </div>
    <div class="signer signer--3">
      <svg class="signer-mark" viewBox="0 0 200 64" role="img" aria-label="Unterschrift Felix Brumholt"><rect x="10" y="22" width="180" height="22" rx="11" fill="rgba(0,0,0,0.06)"/></svg>
      <p class="signer-name">Felix Brumholt</p>
    </div>

    <address class="address" style="font-style:normal">Brumholt Profile GmbH<br>Leistenfabrik-Holzimport<br>Am Sägewerk 4<br>77000 Musterbach-Tal</address>
    <div class="contact">Tel.: 0700 / 1234560<br>Fax: 0700 / 1234569<br>info@brumholt-profile.example</div>

    <div class="back-band">www.brumholt-profile.example</div>
  </section>
</main>
</body>
</html>
```